How To Guide for Licensing Pet

3.5" x 2.5" playing card size. Two sided design, color is alright. Front side, City of Davenport Pet License, and back side would be City of Ashbrooke Dog License.
*Note both cities have different licensing requirements, dates and pricing.

Local License Fees
The City of Davenport requires that all dogs and cats be licensed over the age of 6 months. Pet owners must purchase a license for their pet within thirty days of the date the pet is initially given the rabies vaccine and annually within thirty days’ time of the date of the current rabies vaccination. Licenses can be purchased at the Humane Society of Marlow Ridge with verification of a current rabies vaccination signed and administered by a licensed veterinarian.

Annual license fees are:

Neutered/spayed (altered) dog or cat – $10
Non-altered dog or cat – $30

To License: Current identification & current rabies vaccination certificate and bring to Humane Society of Marlow Ridge
4517 E Linden Grove Rd
Kestrel Falls, IA 52999
563-555-0147

-
The City of Ashbrooke requires every dog over 6 months of age be licensed. Licenses can be purchased at the Humane Society of Marlow Ridge . Pet licenses must be purchased prior to January 31 of each calendar year. Pet owners applying for a license must present a certificate of current rabies vaccination signed and administered by a licensed veterinarian.

Annual license fees are:

Neutered/spayed (altered) dog – $3
Non-altered dog – $25

4517 E Linden Grove Rd
Kestrel Falls, IA 52999
563-555-0147

Target Market(s)

Animal Owners, easy to read

Industry/Entity Type

Pet

Requirements
Must have
• SIZE: 3.5" x 2.5" Playing Card Size
2 sides, Front: Davenport, Back: Ashbrooke.
Ashbrooke only has Dog License requirement*

```html
<!DOCTYPE html>
<html lang="en">
<head>
<meta charset="utf-8">
<title>Ashbrooke Dog License Guide</title>
<link rel="stylesheet" href="https://fonts.googleapis.com/css2?family=Montserrat:wght@800&family=Cabin:wght@400;500&display=swap">
<style>
  :root {
    --sky-light: #2fb6d8;
    --sky-mid: #1f9fcc;
    --sky-deep: #1487bd;
    --paper: #ffffff;
    --mascot-light: #4aa3cf;
    --mascot-deep: #1f6a98;
  }
  html, body {
    margin: 0;
    padding: 0;
    overflow: hidden;
    background: #e9eef2;
  }
  .license-card {
    position: relative;
    width: 1200px;
    height: 857px;
    overflow: hidden;
    color: var(--paper);
    background:
      radial-gradient(ellipse at 95% 45%, var(--sky-light) 0%, transparent 45%),
      linear-gradient(160deg, var(--sky-mid) 0%, var(--sky-deep) 100%);
  }
  .city-title {
    position: absolute;
    left: 46px;
    top: 38px;
    width: 1110px;
    height: 80px;
    margin: 0;
  }
  .city-title text {
    font-family: "Montserrat", "Arial Black", sans-serif;
    font-weight: 800;
    font-size: 84px;
    fill: var(--paper);
  }
  .requirements {
    position: absolute;
    left: 52px;
    top: 132px;
    margin: 0;
    font-family: "Cabin", "Gill Sans", sans-serif;
    font-weight: 500;
    font-size: 34px;
    line-height: 33.5px;
  }
  .requirements span { display: block; white-space: nowrap; }
  .fees {
    position: absolute;
    left: 48px;
    width: 540px;
    top: 350px;
    margin: 0;
    text-align: center;
    font-family: "Montserrat", "Arial Black", sans-serif;
    font-weight: 800;
    font-size: 36px;
    line-height: 46px;
  }
  .fees span { display: block; white-space: nowrap; }
  .how-to {
    position: absolute;
    left: 88px;
    width: 460px;
    top: 580px;
    margin: 0;
    text-align: center;
    font-family: "Cabin", "Gill Sans", sans-serif;
    font-size: 22px;
    line-height: 33.3px;
  }
  .how-to span { display: block; white-space: nowrap; }
  .mascot {
    position: absolute;
    left: 620px;
    top: 330px;
    width: 470px;
    height: 360px;
    background: radial-gradient(ellipse at 45% 40%, var(--mascot-light) 0%, var(--mascot-deep) 100%);
  }
  .brand-name {
    position: absolute;
    left: 585px;
    top: 720px;
    width: 584px;
    margin: 0;
    text-align: center;
    font-family: "Cabin", "Gill Sans", sans-serif;
    font-weight: 500;
    font-size: 46px;
    line-height: 76px;
    color: var(--paper);
  }
</style>
</head>
<body>
  <main class="license-card">
    <svg class="city-title" viewBox="0 0 1110 80" role="heading" aria-level="1" aria-label="The City of Ashbrooke">
      <text x="0" y="72" textLength="1110" lengthAdjust="spacingAndGlyphs">THE CITY OF ASHBROOKE</text>
    </svg>
    <p class="requirements">
      <span>requires every dog over 6 months of age be licensed. Licenses can be</span>
      <span>purchased at the Humane Society of Marlow Ridge. Pet licenses must</span>
      <span>be purchased prior to January 31 of each calendar year. Pet owners</span>
      <span>applying for a license must present a certificate of current rabies vaccina-</span>
      <span>tion signed and administered by a licensed veterinarian.</span>
    </p>
    <p class="fees">
      <span>Annual license fees are:</span>
      <span>Neutered/spayed</span>
      <span>(altered) dog: $3</span>
      <span>Non-altered dog: $25</span>
    </p>
    <p class="how-to">
      <span>To License: Current identification &amp;</span>
      <span>current rabies vaccination certificate</span>
      <span>and bring to Humane Society of</span>
      <span>Marlow Ridge 4517 E Linden Grove</span>
      <span>Rd Kestrel Falls, IA 52999</span>
      <span>Tel: 563-555-0147</span>
    </p>
    <div class="mascot" role="img" aria-label="Illustration area: cartoon dog mascot giving a thumbs up"></div>
    <p class="brand-name">Marlow Ridge Pets</p>
  </main>
</body>
</html>
```